Corporate Design für eine Hautarztpraxis gesucht
Die Zusammenarbeit mit TELUVI war geprägt von höchster Professionalität. Als erstes natürlich das Ergebnis, die Aussagekraft und die Anmutung des entworfenen Designs, da wurden die Anforderungen zu 100 % umgesetzt. Top-Kreativer mit Einfühlungsvermögen in den Kundenwunsch. Als zweites die Zusammenarbeit; verbindliche Kommunikation, die Designentwürfe wurden von TELUVI erklärt und er scheut nicht davor zurück, mitzuteilen wenn die Änderungswünsche vom Briefing und seiner Vorstellung der Umsetzung abweichen, prompte Reaktion auf Kommentare Als drittes die Zuverlässigkeit; alle Zusagen wurden eingehalten, auch das Feintuning nach Projektende war vorbildlich. Zusammenfassend: Top Designer, Vollprofi und 100% Zufriedenheit, danke und jederzeit gerne wieder!!! Working with TELUVI in the project was highly professional. First of all the result and the appearance of the logo and the printproducts; the job fullfillment has reached 100%. TELUVI is a top-creative with understanding and feeling for customer needs. Secondly working with him; the drafts were explained, communication to the point and fast responses to the remarks, and he was free in telling his opinion, if the remarks would lead in the wrong direction Third the reliability; everything was delivered, nothing missed, also the work and finetuning after the official end of the project was to our full satisfaction. Conclusion: Top designer, a real pro, 100 % satisfaction, thanks a lot and we would do it always again!!!
Zielgruppe
Neugründung einer Hautarztpraxis (Gemeinschaftspraxis) von drei Ärzten/Innen
Angeboten wird ein umfassendes medizinisches Spektrum für Kassen- und Privatpatienten sowie Dienstleistungen im Bereich Dermatologischer Kosmetik (Anti Aging, Lasertherapie, Botox, ...)
Die Zielgruppe besteht also zum einen Teil aus Patienten mit gesundheitlichen Problemen der Haut und Allergien sowie andererseits aus Kunden die kosmetische Dienstleistungen nachfragen.
Aufgabenstellung
In Bezug auf die Gestaltung sind wir sehr offen und haben noch keine konkrete Vorstellung, freuen uns aber über viele kreative Vorschläge, von denen wir uns den initialen Impuls für das Design des zukünftigen Logos erhoffen, welches dann im Projekt entwickelt werden soll.
Das Logo soll auf jeden Fall aus einer Wort- und Bildmarke bestehen (Prio 1), eventuell in ein Wappen/Emblem eingebunden sein (Prio 2).
Die Haut als menschliches Organ hat vielschichtige Funktionen, sie schützt den Organismus vor äußeren Umwelteinflüssen und repräsentiert den Menschen nach außen.
Die Haut steht auch für Sensibilität, Reinheit und Schönheit, diese Attribute könnten sich im Logo wiederfinden.
Das Logo soll Kompetenz, Seriosität, Eleganz und Sympathie ausstrahlen, dem Kunden Vertrauen vermitteln und im Verhältnis zur Wortmarke gleich stark sein, so dass z.B. bei der Visitenkarte und dem Briefpapier die Anordnung der Wort- zur Bildmarke unterschiedlich gestaltet werden kann.
Feedback können wir erst in den Abendstunden geben, da tagsüber gearbeitet werden muss und das aktuell noch in unterschiedlichen Arztpraxen.

```html
<!DOCTYPE html>
<html lang="de">
<head>
<meta charset="utf-8">
<title>dermavista – Corporate Design</title>
<link href="https://fonts.googleapis.com/css2?family=Questrial&display=swap" rel="stylesheet">
<style>
  :root {
    --ink: #3d5266;
    --lime: #99ff33;
    --paper: #ffffff;
  }
  * { margin: 0; padding: 0; box-sizing: border-box; }
  html, body { width: 881px; height: 1200px; overflow: hidden; background: var(--paper); }
  body { position: relative; font-family: "Questrial", sans-serif; color: var(--ink); }
  .abs { position: absolute; white-space: nowrap; line-height: 1; }

  .section-label { font-size: 12.5px; }

  .wordmark { color: var(--lime); font-size: 16px; text-align: center; }
  .wordmark-city { color: var(--ink); font-size: 12px; text-align: center; }

  .card {
    position: absolute; left: 195px; width: 272px; height: 273px;
    border: 1px solid var(--ink); border-radius: 20px; overflow: hidden;
  }
  .card--contact { top: 359px; background: var(--paper); }
  .card--appointment { top: 652px; background: var(--lime); }
  .card .abs { font-size: 12.5px; }
  .card .wordmark { font-size: 16px; }
  .card .wordmark-city { font-size: 12px; }
  .appointment-box { position: absolute; left: 41px; top: 47px; width: 191px; height: 102px; background: var(--paper); }

  .letterhead {
    position: absolute; left: 501px; top: 365px; width: 339px; height: 479px;
    border: 0.6px solid var(--ink); background: var(--paper);
  }
  .letterhead .wordmark { font-size: 6.4px; }
  .letterhead .wordmark-city { font-size: 4.6px; }
  .doctor-list { font-size: 4.6px; }
  .sender-line { font-size: 3.8px; }
  .footer-line { font-size: 4px; text-align: center; width: 339px; left: 0; }
  .footer-rule { position: absolute; left: 0; width: 100%; top: 462px; height: 1px; background: var(--ink); }
</style>
</head>
<body>

  <span class="abs section-label" style="left:52px; top:300px;">Logo</span>
  <span class="abs section-label" style="left:195px; top:300px;">Visitenkarten</span>
  <span class="abs section-label" style="left:501px; top:300px;">Briefpapier</span>

  <div class="abs wordmark" style="left:52px; top:405px; width:109px;">dermavista</div>
  <div class="abs wordmark-city" style="left:52px; top:422px; width:109px;">Auenbrück</div>

  <section class="card card--contact">
    <div class="abs wordmark" style="left:0; top:84px; width:272px;">dermavista</div>
    <div class="abs wordmark-city" style="left:0; top:101px; width:272px;">Auenbrück</div>
    <div class="abs" style="left:0; top:149px; width:272px; text-align:center;">Dr.med. Max Mustermann</div>
    <div class="abs" style="left:92px; top:189px;">Musterstraße 00</div>
    <div class="abs" style="left:92px; top:204px;">12345 Auenbrück</div>
    <div class="abs" style="left:71px; top:222px;">T.</div>
    <div class="abs" style="left:92px; top:222px;">01234.56789</div>
    <div class="abs" style="left:71px; top:237px;">M.</div>
    <div class="abs" style="left:92px; top:237px;">kontakt@domain.de</div>
    <div class="abs" style="left:71px; top:252px;">W.</div>
    <div class="abs" style="left:92px; top:252px;">www.domain.de</div>
  </section>

  <section class="card card--appointment">
    <div class="abs" style="left:41px; top:28px;">Ihr nächster Termin:</div>
    <div class="appointment-box"></div>
    <div class="abs" style="left:41px; top:169px;">Sprechzeiten</div>
    <div class="abs" style="left:41px; top:184px;">Mo.</div><div class="abs" style="left:69px; top:184px;">8.00 – 13.00</div><div class="abs" style="left:166px; top:184px;">14.00 –18.00</div>
    <div class="abs" style="left:41px; top:199px;">Di.</div><div class="abs" style="left:69px; top:199px;">8.00 – 13.00</div><div class="abs" style="left:166px; top:199px;">14.00 –18.00</div>
    <div class="abs" style="left:41px; top:214px;">Mi.</div><div class="abs" style="left:69px; top:214px;">8.00 – 13.00</div>
    <div class="abs" style="left:41px; top:228px;">Do.</div><div class="abs" style="left:69px; top:228px;">8.00 – 13.00</div><div class="abs" style="left:166px; top:228px;">15.00 –19.00</div>
    <div class="abs" style="left:41px; top:243px;">Fr.</div><div class="abs" style="left:69px; top:243px;">8.00 – 13.00</div>
  </section>

  <section class="letterhead">
    <div class="abs wordmark" style="left:272px; top:40px; width:52px;">dermavista</div>
    <div class="abs wordmark-city" style="left:272px; top:47px; width:52px;">Auenbrück</div>
    <div class="abs doctor-list" style="left:271px; top:65px;">Dr.med. Max Mustermann</div>
    <div class="abs doctor-list" style="left:271px; top:72px;">Dr.med. Max Mustermann</div>
    <div class="abs doctor-list" style="left:271px; top:80px;">Dr.med. Max Mustermann</div>
    <div class="abs doctor-list" style="left:271px; top:87px;">Dr.med. Max Mustermann</div>
    <div class="abs sender-line" style="left:40px; top:75px;">dermavista – Auenbrück – Musterstraße 00 – 12345 Auenbrück</div>

    <div class="abs footer-line" style="top:444px;">Musterstraße 00 – 12345 Auenbrück – T. 01234.56789 – M. kontakt@domain.de – W. www.domain.de</div>
    <div class="abs footer-line" style="top:450px;">IBAN. DExx xxxx xxxx xxxx xxxx – BIC. xxx xxx xxx – Bank Musterkasse eG – Ärztekammer. xyz</div>
    <div class="footer-rule"></div>
  </section>

</body>
</html>
```